Web Design for Harbor Ledger Associates

Harbor Ledger Associates needs the photoshop files for a simple, clean and professional website design. The company is building a network of bookkeepers/accountants to handle outsourced bookkeeping services for start ups and small businesses. It needs to both attract bookkeepers to become partners and give clients confidence in the professional network. The partners will use products like Tallymint Web, Brightcolumn.com and MintyLedger.com for start ups, as well as help with tasks using the clients existing accounting software.

A home and subpage design is needed. I'll award the work based on the home design. The minor subpage changes can be worked out in the workroom stage.

The pages for the navigation will be: Home, Services, Locations, Partners, FAQ, Contact

```html
<!DOCTYPE html>
<html lang="en">
<head>
<meta charset="utf-8">
<title>Harbor Ledger Associates</title>
<link rel="stylesheet" href="https://fonts.googleapis.com/css2?family=Catamaran:wght@400;500;600;700&family=Gafata&display=swap">
<style>
:root{
  --blue:#1a9bd7;
  --ink:#4a4b4e;
  --muted:#707174;
  --slate:#5c5d60;
  --paper:#f4f4f4;
  --white:#ffffff;
  --rule:#dcdcdc;
  --partner:#a9aaad;
}
*{box-sizing:border-box;margin:0;padding:0}
html,body{width:1040px;height:1200px;overflow:hidden}
body{position:relative;background:var(--paper);font-family:"Gafata",sans-serif;color:var(--ink)}
.abs{position:absolute}
.site-header{position:absolute;left:0;top:0;width:1040px;height:77px;background:#f7f8f9;border-bottom:1px solid #e6e7e8}
.brand{position:absolute;left:138px;top:17px;display:flex;align-items:center;gap:10px}
.brand-square{width:34px;height:34px;border:3px solid var(--blue)}
.brand-name{font-family:"Catamaran",sans-serif;font-weight:700;color:var(--blue);font-size:15px;line-height:14px;letter-spacing:.3px;width:120px}
.main-nav{position:absolute;left:478px;top:31px;display:flex;gap:23px;font-family:"Catamaran",sans-serif;font-size:10.5px;color:var(--ink);letter-spacing:.3px}
.nav-divider{position:absolute;left:865px;top:26px;width:1px;height:26px;background:var(--ink)}
.search-icon{position:absolute;left:878px;top:25px}
.hero{position:absolute;left:0;top:77px;width:1040px;height:383px;background:linear-gradient(110deg,#d6dde5 0%,#e8ecf1 35%,#dfe6ee 60%,#cfd8e2 100%)}
.hero-title{position:absolute;left:0;width:1040px;text-align:center;top:80px;font-family:"Catamaran",sans-serif;font-weight:400;font-size:38px;color:var(--slate);letter-spacing:-.3px}
.hero-sub{position:absolute;left:0;width:1040px;text-align:center;top:121px;font-family:"Catamaran",sans-serif;font-size:21px;color:var(--slate);letter-spacing:-.2px}
.cta-label{position:absolute;top:199px;width:225px;text-align:center;font-family:"Catamaran",sans-serif;font-weight:600;font-size:17.5px}
.cta-label.register{left:253px;color:var(--blue)}
.cta-label.hire{left:557px;color:var(--slate)}
.cta-btn{position:absolute;top:230px;width:225px;height:45px;display:flex;align-items:center;justify-content:center;color:var(--white);font-family:"Catamaran",sans-serif;font-weight:600;font-size:17px;letter-spacing:.3px;border-radius:2px}
.cta-btn.register{left:253px;background:var(--blue)}
.cta-btn.hire{left:557px;background:var(--slate)}
.or-line{position:absolute;top:252px;height:1px;width:13px;background:#9aa}
.or-badge{position:absolute;left:500px;top:234px;width:36px;height:36px;border-radius:50%;background:var(--white);display:flex;align-items:center;justify-content:center;font-family:"Catamaran",sans-serif;font-weight:700;font-size:10.5px;color:var(--ink)}
.section-title{font-family:"Catamaran",sans-serif;font-weight:600;font-size:19.5px;letter-spacing:-.2px}
.featured-title{position:absolute;left:141px;top:502px;color:var(--blue)}
.card{position:absolute;width:213px;height:171px;background:var(--white);border:1px solid #ececec}
.card-head{position:absolute;left:0;top:0;width:100%;height:74px;background:var(--slate)}
.card-photo{position:absolute;left:17px;top:8px;width:77px;height:77px;border:3px solid var(--white);background:linear-gradient(160deg,#b48e77,#6f5a4f 60%,#3f3a3a)}
.card-name{position:absolute;left:106px;top:11px;font-family:"Catamaran",sans-serif;font-weight:600;font-size:14px;color:var(--white)}
.hire-btn{position:absolute;left:106px;top:37px;width:81px;height:28px;background:var(--blue);color:var(--white);font-family:"Catamaran",sans-serif;font-weight:600;font-size:11.5px;display:flex;align-items:center;justify-content:center;letter-spacing:.3px}
.card-facts{position:absolute;left:18px;top:96px;font-size:10.5px;line-height:18.5px}
.card-facts dt{position:absolute;left:0;color:var(--muted)}
.card-facts dd{margin-left:77px;color:var(--ink)}
.card-facts dd.rate{font-family:"Catamaran",sans-serif;font-size:13.5px}
.requests{position:absolute;left:619px;top:452px;width:285px;height:449px;background:var(--white)}
.results-count{position:absolute;left:30px;top:19px;font-size:10.5px;color:var(--muted)}
.requests-title{position:absolute;left:28px;top:50px;color:var(--slate)}
.job{position:absolute;left:28px;width:241px;height:112px;border-bottom:1px solid var(--rule)}
.job-title{font-family:"Catamaran",sans-serif;font-size:13px;color:var(--blue)}
.job-company{font-size:10.5px;color:var(--ink);margin-top:1px}
.job-meta{position:absolute;left:0;font-size:10px;color:var(--ink);display:flex;align-items:center;gap:5px}
.job-meta svg{flex:none}
.more-jobs{position:absolute;left:28px;top:422px;display:flex;align-items:center;gap:8px;font-family:"Catamaran",sans-serif;font-size:11px;color:var(--ink);text-decoration:underline}
.partners-strip{position:absolute;left:0;top:941px;width:1040px;height:76px;background:var(--white);display:flex;align-items:center;justify-content:space-between;padding:0 135px 0 143px}
.partner-mark{display:flex;align-items:center;gap:6px;font-family:"Catamaran",sans-serif;font-size:16px;color:var(--partner)}
.partner-dot{width:18px;height:18px;border-radius:50%;background:#c8c9cb}
.partner-band{position:absolute;left:0;top:1017px;width:1040px;height:100px;background:var(--slate);color:var(--white)}
.partner-band h2{position:absolute;left:137px;top:23px;font-family:"Catamaran",sans-serif;font-weight:600;font-size:19px;letter-spacing:-.3px}
.partner-band p{position:absolute;left:138px;top:53px;font-size:11.5px;line-height:14px;width:560px}
.signup-free{position:absolute;left:763px;top:45px;width:143px;height:28px;border-radius:14px;background:var(--blue);display:flex;align-items:center;justify-content:center;font-family:"Catamaran",sans-serif;font-weight:600;font-size:11.5px;letter-spacing:.2px}
.site-footer{position:absolute;left:0;top:1117px;width:1040px;height:83px;background:var(--paper)}
.footer-nav{position:absolute;left:138px;top:32px;font-size:9.5px;color:var(--ink);letter-spacing:.2px}
.copyright{position:absolute;left:138px;top:51px;font-size:9.5px;color:var(--muted)}
.social{position:absolute;left:560px;top:34px;display:flex;gap:12px;font-family:"Catamaran",sans-serif;font-size:9px;color:#8a8b8e}
.footer-brand{position:absolute;left:790px;top:30px;display:flex;align-items:center;gap:8px}
.footer-brand .brand-square{width:26px;height:26px;border:2px solid #9c9da0}
.footer-brand .brand-name{color:#9c9da0;font-size:10px;line-height:9px;width:80px}
</style>
</head>
<body>

<header class="site-header">
  <div class="brand">
    <span class="brand-square"></span>
    <span class="brand-name">HARBOR LEDGER ASSOCIATES</span>
  </div>
  <nav class="main-nav">
    <span>HOME</span><span>SERVICES</span><span>LOCATIONS</span><span>PARTNERS</span><span>FAQ</span><span>CONTACT</span>
  </nav>
  <span class="nav-divider"></span>
  <svg class="search-icon" width="28" height="28" viewBox="0 0 28 28" aria-hidden="true">
    <circle cx="11" cy="11" r="8" fill="none" stroke="#222" stroke-width="2.4"/>
    <line x1="17" y1="17" x2="25" y2="25" stroke="#222" stroke-width="3.5" stroke-linecap="round"/>
  </svg>
</header>

<section class="hero" role="img" aria-label="Soft blurred photo of two professionals shaking hands over a tablet">
  <h1 class="hero-title">ACCOUNTANTS &amp; BOOKKEEPERS</h1>
  <p class="hero-sub">YOUR PRACTICE. YOUR CLIENTS. ONE PLATFORM</p>
  <div class="cta-label register">REGISTER AS ACCOUNTANT</div>
  <div class="cta-label hire">HIRE AN ACCOUNTANT</div>
  <a class="cta-btn register">REGISTER NOW!</a>
  <span class="or-line" style="left:484px"></span>
  <span class="or-badge">OR</span>
  <span class="or-line" style="left:540px"></span>
  <a class="cta-btn hire">SIGN UP NOW!</a>
</section>

<h2 class="section-title featured-title">FEATURED ACCOUNTANTS</h2>

<article class="card" style="left:138px;top:542px">
  <div class="card-head"></div>
  <div class="card-photo" role="img" aria-label="Portrait photo of accountant Owen Marlow"></div>
  <div class="card-name">Owen Marlow</div>
  <a class="hire-btn">HIRE ME</a>
  <dl class="card-facts"><dt>Qualification:</dt><dd>CAAP, America</dd><dt>Experience:</dt><dd>10 Years</dd><dt>Hourly Rate:</dt><dd class="rate">$25/Hour</dd></dl>
</article>
<article class="card" style="left:369px;top:542px">
  <div class="card-head"></div>
  <div class="card-photo" role="img" aria-label="Portrait photo of accountant Talia Brooks" style="background:linear-gradient(160deg,#d9a98a,#8a4b3a 55%,#5a2f33)"></div>
  <div class="card-name">Talia Brooks</div>
  <a class="hire-btn">HIRE ME</a>
  <dl class="card-facts"><dt>Qualification:</dt><dd>CAAP, America</dd><dt>Experience:</dt><dd>10 Years</dd><dt>Hourly Rate:</dt><dd class="rate">$25/Hour</dd></dl>
</article>
<article class="card" style="left:138px;top:730px">
  <div class="card-head"></div>
  <div class="card-photo" role="img" aria-label="Portrait photo of accountant Marisol" style="background:linear-gradient(160deg,#6b7d56,#b08770 50%,#5a2a2a)"></div>
  <div class="card-name">Marisol</div>
  <a class="hire-btn">HIRE ME</a>
  <dl class="card-facts"><dt>Qualification:</dt><dd>CAAP, America</dd><dt>Experience:</dt><dd>10 Years</dd><dt>Hourly Rate:</dt><dd class="rate">$25/Hour</dd></dl>
</article>
<article class="card" style="left:369px;top:730px">
  <div class="card-head"></div>
  <div class="card-photo" role="img" aria-label="Portrait photo of accountant Dean Whitaker" style="background:linear-gradient(160deg,#8c8e8a,#c09a84 50%,#6c6f73)"></div>
  <div class="card-name">Dean Whitaker</div>
  <a class="hire-btn">HIRE ME</a>
  <dl class="card-facts"><dt>Qualification:</dt><dd>CAAP, America</dd><dt>Experience:</dt><dd>10 Years</dd><dt>Hourly Rate:</dt><dd class="rate">$25/Hour</dd></dl>
</article>

<aside class="requests">
  <div class="results-count">1-15 of 13750 Results</div>
  <h2 class="section-title requests-title">SERVICE REQUESTS</h2>

  <div class="job" style="top:90px">
    <div class="job-title">Staff Accountant - Payroll</div>
    <div class="job-company">Kestrel Care Facilities</div>
    <div class="job-meta" style="top:44px"><svg width="12" height="11" viewBox="0 0 12 11"><rect x="1" y="3" width="10" height="7" fill="none" stroke="#444" stroke-width="1.2"/><circle cx="6" cy="6.5" r="1.6" fill="#444"/><line x1="3" y1="1.5" x2="9" y2="1.5" stroke="#444"/></svg>Competitive</div>
    <div class="job-meta" style="top:44px;left:128px"><svg width="10" height="12" viewBox="0 0 10 12"><path d="M5 11.5C2 7.5 1 6 1 4.3a4 4 0 0 1 8 0C9 6 8 7.5 5 11.5z" fill="#444"/><circle cx="5" cy="4.3" r="1.4" fill="#fff"/></svg>Austin, TX</div>
    <div class="job-meta" style="top:63px"><svg width="11" height="11" viewBox="0 0 11 11"><circle cx="5.5" cy="5.5" r="4.6" fill="none" stroke="#444" stroke-width="1.2"/><path d="M5.5 2.8v2.9h2" fill="none" stroke="#444" stroke-width="1.2"/></svg>Permanent, Full time</div>
    <div class="job-meta" style="top:63px;left:128px"><svg width="12" height="11" viewBox="0 0 12 11"><rect x="1" y="2" width="10" height="8.4" fill="none" stroke="#444" stroke-width="1.2"/><line x1="1" y1="4.3" x2="11" y2="4.3" stroke="#444" stroke-width="1.2"/><line x1="3.5" y1="0.5" x2="3.5" y2="2.5" stroke="#444"/><line x1="8.5" y1="0.5" x2="8.5" y2="2.5" stroke="#444"/></svg>Posted on: 02 Jun 14</div>
  </div>

  <div class="job" style="top:198px">
    <div class="job-title">Client Accounting Manager</div>
    <div class="job-company">Pryce Holloway &amp; Company, LLC</div>
    <div class="job-meta" style="top:44px"><svg width="12" height="11" viewBox="0 0 12 11"><rect x="1" y="3" width="10" height="7" fill="none" stroke="#444" stroke-width="1.2"/><circle cx="6" cy="6.5" r="1.6" fill="#444"/><line x1="3" y1="1.5" x2="9" y2="1.5" stroke="#444"/></svg>Competitive</div>
    <div class="job-meta" style="top:44px;left:128px"><svg width="10" height="12" viewBox="0 0 10 12"><path d="M5 11.5C2 7.5 1 6 1 4.3a4 4 0 0 1 8 0C9 6 8 7.5 5 11.5z" fill="#444"/><circle cx="5" cy="4.3" r="1.4" fill="#fff"/></svg>Alexandria, LA</div>
    <div class="job-meta" style="top:63px"><svg width="11" height="11" viewBox="0 0 11 11"><circle cx="5.5" cy="5.5" r="4.6" fill="none" stroke="#444" stroke-width="1.2"/><path d="M5.5 2.8v2.9h2" fill="none" stroke="#444" stroke-width="1.2"/></svg>Permanent, Full time</div>
    <div class="job-meta" style="top:63px;left:128px"><svg width="12" height="11" viewBox="0 0 12 11"><rect x="1" y="2" width="10" height="8.4" fill="none" stroke="#444" stroke-width="1.2"/><line x1="1" y1="4.3" x2="11" y2="4.3" stroke="#444" stroke-width="1.2"/><line x1="3.5" y1="0.5" x2="3.5" y2="2.5" stroke="#444"/><line x1="8.5" y1="0.5" x2="8.5" y2="2.5" stroke="#444"/></svg>Posted on: 02 Jun 14</div>
  </div>

  <div class="job" style="top:312px">
    <div class="job-title">Audit Senior Manager</div>
    <div class="job-company">Varden &amp; Quill</div>
    <div class="job-meta" style="top:44px"><svg width="12" height="11" viewBox="0 0 12 11"><rect x="1" y="3" width="10" height="7" fill="none" stroke="#444" stroke-width="1.2"/><circle cx="6" cy="6.5" r="1.6" fill="#444"/><line x1="3" y1="1.5" x2="9" y2="1.5" stroke="#444"/></svg>Competitive</div>
    <div class="job-meta" style="top:44px;left:128px"><svg width="10" height="12" viewBox="0 0 10 12"><path d="M5 11.5C2 7.5 1 6 1 4.3a4 4 0 0 1 8 0C9 6 8 7.5 5 11.5z" fill="#444"/><circle cx="5" cy="4.3" r="1.4" fill="#fff"/></svg>Riverside, CA</div>
    <div class="job-meta" style="top:63px"><svg width="11" height="11" viewBox="0 0 11 11"><circle cx="5.5" cy="5.5" r="4.6" fill="none" stroke="#444" stroke-width="1.2"/><path d="M5.5 2.8v2.9h2" fill="none" stroke="#444" stroke-width="1.2"/></svg>Permanent, Full time</div>
    <div class="job-meta" style="top:63px;left:128px"><svg width="12" height="11" viewBox="0 0 12 11"><rect x="1" y="2" width="10" height="8.4" fill="none" stroke="#444" stroke-width="1.2"/><line x1="1" y1="4.3" x2="11" y2="4.3" stroke="#444" stroke-width="1.2"/><line x1="3.5" y1="0.5" x2="3.5" y2="2.5" stroke="#444"/><line x1="8.5" y1="0.5" x2="8.5" y2="2.5" stroke="#444"/></svg>Posted on: 02 Jun 14</div>
  </div>

  <a class="more-jobs">MORE JOBS
    <svg width="16" height="16" viewBox="0 0 16 16"><circle cx="8" cy="8" r="6.8" fill="none" stroke="#333" stroke-width="1.8"/><path d="M6.6 4.8L9.8 8l-3.2 3.2" fill="none" stroke="#333" stroke-width="1.8"/></svg>
  </a>
</aside>

<section class="partners-strip">
  <span class="partner-mark"><span class="partner-dot"></span>Wavefold</span>
  <span class="partner-mark"><span class="partner-dot"></span>Orchardline</span>
  <span class="partner-mark"><span class="partner-dot"></span>Zenlo</span>
  <span class="partner-mark" style="font-size:13px">Brightcolumn</span>
  <span class="partner-mark">skyledgerbooks</span>
  <span class="partner-mark">MintyLedger</span>
</section>

<section class="partner-band">
  <h2>Partner With Us</h2>
  <p>Partnering with Harbor Ledger lets your clients get the most from your expertise and experience.<br>Together, we can make small business better.</p>
  <a class="signup-free">SIGN UP FOR FREE</a>
</section>

<footer class="site-footer">
  <nav class="footer-nav">HOME / &nbsp;SERVICES &nbsp;/ &nbsp;LOCATIONS / &nbsp;PARTNERS &nbsp;/ &nbsp;FAQ &nbsp;/ &nbsp;CONTACT</nav>
  <div class="copyright">Copyright © HARBORLEDGERASSOCIATES. All Right Reserved.</div>
  <div class="social"><span>Pagenook</span><span>Chirply</span><span>Circlet</span><span>Viewreel</span></div>
  <div class="footer-brand">
    <span class="brand-square"></span>
    <span class="brand-name">HARBOR LEDGER ASSOCIATES</span>
  </div>
</footer>

</body>
</html>
```